Leaflets
We supply stone and solid surfaces to the trade and project manage its installation
Project: Leaflets
Leaflets - Construction
Creative Brief
Construction
Architects, Interior designers, property developers, kitchen and bathroom designers, shopfitters Our offer is mainly business to business. Our branding and images are corporate and our content (wording) is more casual (which is what makes us different from the competition)
A leaflet with our branding, logos and fonts to be used as an introduction to our clients mainly targeted trough site visits and by posting samples. Images and branding available on request.

```html
<!DOCTYPE html>
<html lang="en">
<head>
<meta charset="utf-8">
<title>Trelvax – Leaflet inside spread</title>
<link href="https://fonts.googleapis.com/css2?family=Open+Sans:ital,wght@0,400;0,600;0,700;1,400&display=swap" rel="stylesheet">
<style>
  :root {
    --purple: #62287f;
    --purple-text: #6b3290;
    --green: #7cb82f;
    --paper: #ffffff;
    --ink: #4a4a4a;
    --fold: #e3e3e3;
    --photo-stone: linear-gradient(160deg, #d9d6d2 0%, #a9a6a3 55%, #6f6c6a 100%);
    --photo-kitchen: linear-gradient(170deg, #e8e6e2 0%, #b9b4ad 60%, #847d75 100%);
    --photo-home: linear-gradient(165deg, #f0ede8 0%, #c9c2b8 55%, #9b9186 100%);
    --photo-counter: linear-gradient(180deg, #d5d2ce 0%, #8f8a86 50%, #3f3c3b 100%);
  }
  * { box-sizing: border-box; margin: 0; padding: 0; }
  html, body { width: 1200px; height: 874px; overflow: hidden; background: var(--paper); }
  body { font-family: "Open Sans", sans-serif; color: var(--ink); }

  .spread {
    width: 1200px; height: 874px;
    display: grid; grid-template-columns: repeat(3, 400px);
    position: relative;
  }
  .panel { position: relative; display: flex; flex-direction: column; border-right: 1px solid var(--fold); }
  .panel:last-child { border-right: none; }

  .services-band {
    position: absolute; top: 0; left: 400px; width: 800px; height: 46px;
    background: var(--purple); color: #fff;
    display: flex; align-items: center; justify-content: center;
    font-size: 15px; font-weight: 600; letter-spacing: 0.6em; text-transform: uppercase;
    z-index: 2;
  }

  .photo { position: relative; width: 100%; flex: none; }
  .photo-label {
    position: absolute; right: 0; bottom: 14px;
    background: var(--green); color: #fff;
    font-size: 14px; font-weight: 600;
    padding: 6px 18px 6px 22px;
  }
  .panel--about .photo { height: 240px; background: var(--photo-stone); }
  .panel--commercial .photo--top { margin-top: 46px; height: 196px; background: var(--photo-kitchen); }
  .panel--commercial .photo--bottom { height: 250px; background: var(--photo-counter); margin-top: auto; }
  .panel--residential .photo { margin-top: 46px; height: 196px; background: var(--photo-home); }

  .copy { padding: 26px 30px 0; }
  .copy p { font-size: 14.5px; line-height: 1.6; text-align: justify; margin-bottom: 14px; }

  .callout { padding: 4px 30px 0; }
  .callout p { color: var(--purple-text); font-style: italic; font-size: 15px; line-height: 1.55; }

  .sign-off { margin-top: auto; padding: 0 30px 40px; text-align: center; }
  .brand { display: inline-flex; align-items: center; gap: 12px; margin-bottom: 18px; }
  .brand-square { width: 34px; height: 34px; background: var(--green); }
  .brand-name { font-size: 30px; font-weight: 700; color: var(--purple); }
  .contact { font-style: normal; font-size: 13px; line-height: 1.6; color: var(--ink); }
</style>
</head>
<body>
<main class="spread">
  <div class="services-band">Services</div>

  <section class="panel panel--about">
    <div class="photo" role="img" aria-label="Photograph of a modern stone staircase and interior">
      <span class="photo-label">About us</span>
    </div>
    <div class="copy">
      <p>Trelvax supplies stone and solid surfaces to the trade, and we look after the whole installation for you from the first template to the final polish on site.</p>
      <p>We work with architects, interior designers, developers and shopfitters who want a partner that answers the phone, turns up on time and gets it right.</p>
      <p>Every job has one project manager, so you always know who to call and what happens next.</p>
      <p>We keep things simple, honest and friendly, because good work should never feel like hard work.</p>
    </div>
  </section>

  <section class="panel panel--commercial">
    <div class="photo photo--top" role="img" aria-label="Photograph of a commercial kitchen with stone worktops">
      <span class="photo-label">Commercial Sector</span>
    </div>
    <div class="copy">
      <p>From hotel lobbies to busy restaurant counters, our surfaces are made to look sharp and take a beating every single day.</p>
      <p>We cut, finish and fit quartz, granite and solid surface in our own workshop, then install on site with our own fitting teams.</p>
      <p>Samples are free, so ask and we will post them out.</p>
    </div>
    <div class="photo photo--bottom" role="img" aria-label="Photograph of a dark solid surface reception counter"></div>
  </section>

  <section class="panel panel--residential">
    <div class="photo" role="img" aria-label="Photograph of a bright residential kitchen">
      <span class="photo-label">Residential Sector</span>
    </div>
    <div class="copy">
      <p>At home, a worktop is the thing you touch most. We help kitchen and bathroom designers give their clients surfaces they will love for years.</p>
      <p>Tell us the size, the colour and the date, and we will handle the rest.</p>
    </div>
    <div class="callout">
      <p>If you would like samples or a site visit, just give us a call or drop us an email.</p>
    </div>
    <div class="sign-off">
      <div class="brand">
        <span class="brand-square"></span>
        <span class="brand-name">Trelvax</span>
      </div>
      <address class="contact">
        Unit 7, 42 Fenwick Road<br>
        Leeds LS9 4QT<br>
        Phone: 0113 496 0721<br>
        Email: hello@trelvax.co.uk<br>
        www.trelvax.co.uk
      </address>
    </div>
  </section>
</main>
</body>
</html>
```